Crestline Sealing - Logo and Advert

Help to provide logo and advert.
Advert is to be short and concise to fit in a printed directory posted around homes.
Ideally the same advert to be able to be blown up as a leaflet.
Use of eco friendly type colours, soft greens and blues.
Logo to be subtle but indicative to roofing and facades.
Breakdown of advert as follows;
Company name:
Crestline Sealing
Sub title:
Roofing & Façades
Services breakdown:
Pitched (Slating & Tiling)
Flat (Single Ply, Liquid & Mineral Felt)
Hard Metal (Zinc Standing Seam)
Leadwork
Roof lights and lanterns
Generic notes:
100% flame free applications available, eliminating all fire risks to your property. (No gas torch’s etc.).
Expert consultation and advice.
Product warranty and/or insurance backed warranty available.
Fully insured contractor.
Contact information:
Phone number to be confirmed
Email and/or website to be confirmed.
Please feel free to try out different colours and fonts other than outlined. I am not limited to those and open to suggestions.
Target Market(s)
Domestic/Private Home Owners/Small Buidlers
Industry/Entity Type
Roofing
Font styles to use
Look and feel
Each slider illustrates characteristics of the customer's brand and the style your logo design should communicate.

```html
<!DOCTYPE html>
<html lang="en">
<head>
<meta charset="utf-8">
<title>Crestline Sealing – Logo and Advert</title>
<link href="https://fonts.googleapis.com/css2?family=Montserrat:wght@600;700;800&family=Open+Sans:ital,wght@0,400;0,600;0,700;1,600&display=swap" rel="stylesheet">
<style>
:root{
  --board:#4d5b5f;
  --navy:#1f3f95;
  --green:#8cb53f;
  --green-light:#a7cc3c;
  --sky:#b9d8e2;
  --orange:#f7a823;
  --dark:#3a3d40;
  --white:#ffffff;
  --ink:#222;
}
*{margin:0;padding:0;box-sizing:border-box}
html,body{width:1200px;height:798px;overflow:hidden;background:var(--board);font-family:"Open Sans",sans-serif}
.board{position:relative;width:1200px;height:798px}

/* logo card */
.logo-card{position:absolute;left:81px;top:166px;width:460px;height:466px;background:var(--white);
  border-top:5px solid var(--green);border-bottom:5px solid var(--navy);
  display:flex;flex-direction:column;align-items:center;justify-content:center;text-align:center}
.logo-card .mark-dot{width:92px;height:92px;border-radius:50%;background:var(--green-light);margin-bottom:30px}
.brand-name{font-family:"Montserrat",sans-serif;font-weight:800;color:var(--navy);line-height:1}
.logo-card .brand-name{font-size:44px;letter-spacing:1px}
.logo-card .brand-sub{font-family:"Montserrat",sans-serif;font-weight:700;color:var(--navy);font-size:16px;letter-spacing:5px;margin-top:16px}

/* advert */
.advert{position:absolute;left:610px;top:58px;width:524px;height:682px;background:var(--white);overflow:hidden}
.hero-photo{position:absolute;left:0;top:0;width:524px;height:272px;
  background:linear-gradient(100deg,#e9ecef 0%,#d7dde3 38%,#5a6fb0 62%,#3f56a3 100%)}
.headline{position:absolute;left:334px;top:62px;color:var(--white);font-family:"Montserrat",sans-serif;font-weight:800;font-size:34px;line-height:33px;letter-spacing:-.5px}
.hero-tag{position:absolute;left:78px;top:250px;font-size:14px;font-weight:600;color:var(--ink)}
.hero-brand{position:absolute;left:354px;top:236px;width:130px;text-align:center}
.hero-brand .brand-name{font-size:15px}

.services{position:absolute;left:0;top:278px;width:524px;height:258px;background:var(--sky);
  clip-path:polygon(0 0,100% 30px,100% 100%,0 100%)}
.services-tab{position:absolute;left:218px;top:286px;width:93px;height:18px;background:var(--dark);color:var(--white);
  font-size:12px;font-style:italic;font-weight:600;text-align:center;line-height:18px}
.stars{position:absolute;top:287px;color:var(--orange);font-size:9px;letter-spacing:7px}

.photo{position:absolute;border:1px solid #fff}
.ph-lantern{left:22px;top:302px;width:140px;height:111px;background:linear-gradient(180deg,#3d6fc0,#9fb6c9 55%,#4b5358)}
.ph-pitched{left:170px;top:302px;width:235px;height:111px;background:linear-gradient(180deg,#7e8a78,#8b8f96 45%,#a0574a)}
.ph-lead{left:414px;top:302px;width:92px;height:111px;background:linear-gradient(180deg,#6f7476,#2c2f33 60%,#e9e2c8)}
.ph-zinc{left:22px;top:440px;width:90px;height:108px;background:linear-gradient(90deg,#6d7073,#9a9da0,#5f6265)}
.ph-flat{left:418px;top:440px;width:89px;height:108px;background:linear-gradient(160deg,#cfe0ee,#7ea6cf 55%,#d6e4f1)}

.label{position:absolute;background:var(--orange);color:var(--navy);font-size:8.5px;font-weight:700;line-height:10.5px;white-space:nowrap}
.lb-lantern,.lb-pitched,.lb-lead{top:413px;height:18px;text-align:center;line-height:18px;border-radius:0 0 3px 3px}
.lb-lantern{left:34px;width:108px}
.lb-pitched{left:231px;width:113px}
.lb-lead{left:432px;width:53px}
.lb-zinc{left:0;top:535px;width:116px;height:46px;padding:14px 0 0 30px;border-radius:0 0 4px 0}
.lb-flat{left:410px;top:535px;width:114px;height:46px;padding:14px 0 0 8px;border-radius:0 0 0 4px}

.features{position:absolute;left:110px;top:442px;width:308px;height:93px;background:var(--white);border:1px solid #c9dbe3}
.feature{position:absolute;display:flex;gap:5px;font-size:7.2px;line-height:9px;color:var(--ink);white-space:nowrap}
.feature svg{flex:none}
.f-flame{left:6px;top:16px}
.f-warranty{left:123px;top:14px}
.f-advice{left:122px;top:56px;align-items:center}
.f-insured{left:228px;top:56px;align-items:center}

.footer-band{position:absolute;left:0;top:613px;width:524px;height:69px;background:var(--green)}
.footer-badge{position:absolute;left:189px;top:568px;width:145px;height:130px;background:var(--white);border-radius:72px 72px 0 0}
.footer-brand{position:absolute;left:189px;top:620px;width:145px;text-align:center}
.footer-brand .brand-name{font-size:17px}
.footer-brand .brand-sub{font-family:"Montserrat",sans-serif;font-weight:700;color:var(--navy);font-size:7px;letter-spacing:1.5px;margin-top:4px}
.contact{position:absolute;display:flex;align-items:center;gap:8px;color:var(--white);font-size:10.5px;font-weight:600;white-space:nowrap}
.contact .ico{width:17px;height:17px;border-radius:50%;background:var(--navy);display:flex;align-items:center;justify-content:center}
.c-address{left:15px;top:628px}
.c-phone{left:15px;top:652px}
.c-email{left:344px;top:628px}
.c-web{left:344px;top:652px}
</style>
</head>
<body>
<main class="board">

  <section class="logo-card" aria-label="Crestline Sealing logo">
    <div class="mark-dot"></div>
    <div class="brand-name">CRESTLINE SEALING</div>
    <div class="brand-sub">Roofing &amp; Façades</div>
  </section>

  <article class="advert">
    <div class="hero-photo" role="img" aria-label="Photo of a hand held protectively above a model house with a tiled roof, on a blue backdrop"></div>
    <h1 class="headline">say<br>goodbye<br>to water<br>leakage</h1>
    <p class="hero-tag">Complete waterproofing solution from</p>
    <div class="hero-brand"><div class="brand-name">CRESTLINE SEALING</div></div>

    <div class="services"></div>
    <span class="stars" style="left:170px">★★★</span>
    <div class="services-tab">Our services</div>
    <span class="stars" style="left:322px">★★★</span>

    <div class="photo ph-lantern" role="img" aria-label="Photo of a glass roof lantern on a flat roof"></div>
    <div class="photo ph-pitched" role="img" aria-label="Photo of a pitched tiled roof on a brick house"></div>
    <div class="photo ph-lead" role="img" aria-label="Photo of leadwork flashing on a roof edge"></div>
    <div class="label lb-lantern">Roof lights and lanterns</div>
    <div class="label lb-pitched">Pitched (Slating &amp; Tiling)</div>
    <div class="label lb-lead">Leadwork</div>

    <div class="label lb-zinc">Hard Metal (Zinc<br>Standing Seam)</div>
    <div class="label lb-flat">Flat (Single Ply,<br>Liquid &amp; Mineral Felt)</div>
    <div class="photo ph-zinc" role="img" aria-label="Photo of zinc standing seam metal cladding"></div>

    <div class="features">
      <div class="feature f-flame">
        <svg width="24" height="24" viewBox="0 0 26 26"><circle cx="13" cy="13" r="11" fill="none" stroke="var(--navy)" stroke-width="2"/><path d="M13 6c3 4 5 6 5 9a5 5 0 0 1-10 0c0-2 1-3 2-4 0 2 1 3 2 3-1-3 0-6 1-8z" fill="var(--navy)"/><line x1="5" y1="5" x2="21" y2="21" stroke="var(--navy)" stroke-width="2"/></svg>
        <span>100% flame free<br>applications available,<br>eliminating all fire risks<br>to your property.<br>(No gas torch’s etc.).</span>
      </div>
      <div class="feature f-warranty">
        <svg width="20" height="26" viewBox="0 0 22 28"><path d="M6 16l-3 10 5-3 3 4 0-10zM16 16l3 10-5-3-3 4 0-10z" fill="var(--navy)"/><circle cx="11" cy="10" r="9" fill="var(--navy)"/><path d="M6.5 10l3 3 6-6" fill="none" stroke="#fff" stroke-width="2"/></svg>
        <span>Product warranty and/or insurance<br>backed warranty available.</span>
      </div>
      <div class="feature f-advice">
        <svg width="24" height="24" viewBox="0 0 26 26"><path d="M13 3a10 9 0 1 1-6 16l-4 3 1-5A10 9 0 0 1 13 3z" fill="none" stroke="var(--navy)" stroke-width="2"/><circle cx="8.5" cy="12" r="1.7" fill="var(--navy)"/><circle cx="13" cy="12" r="1.7" fill="var(--navy)"/><circle cx="17.5" cy="12" r="1.7" fill="var(--navy)"/></svg>
        <span>Expert consultation<br>and advice.</span>
      </div>
      <div class="feature f-insured">
        <svg width="20" height="22" viewBox="0 0 22 24"><path d="M11 2l8 3v7c0 5-4 9-8 10-4-1-8-5-8-10V5z" fill="none" stroke="var(--navy)" stroke-width="2"/><path d="M11 5l5 2v5c0 3-2 6-5 7z" fill="var(--navy)"/></svg>
        <span>Fully insured<br>contractor.</span>
      </div>
    </div>
    <div class="photo ph-flat" role="img" aria-label="Photo of a waterproof membrane roll with water droplets"></div>

    <div class="footer-band"></div>
    <div class="footer-badge"></div>
    <div class="footer-brand">
      <div class="brand-name">CRESTLINE<br>SEALING</div>
      <div class="brand-sub">Roofing &amp; Façades</div>
    </div>

    <div class="contact c-address"><span class="ico"><svg width="11" height="11" viewBox="0 0 12 12"><path d="M1 6l5-4.5L11 6M2.5 5v5.5h7V5" fill="none" stroke="#fff" stroke-width="1.4"/></svg></span>Landmark, Office address.</div>
    <div class="contact c-phone"><span class="ico"><svg width="10" height="10" viewBox="0 0 12 12"><path d="M2 1h3l1 3-1.5 1a7 7 0 0 0 3 3L9 6.5l3 1v3l-1 1C6 11.5.5 6 .5 2z" fill="#fff"/></svg></span>+123-456-789 I +123-456-789</div>
    <div class="contact c-email"><span class="ico" style="font-size:10px">@</span>hello@crestlinesealing.com</div>
    <div class="contact c-web"><span class="ico"><svg width="11" height="11" viewBox="0 0 12 12"><circle cx="6" cy="6" r="5" fill="none" stroke="#fff" stroke-width="1.2"/><ellipse cx="6" cy="6" rx="2.2" ry="5" fill="none" stroke="#fff" stroke-width="1"/><line x1="1" y1="6" x2="11" y2="6" stroke="#fff" stroke-width="1"/></svg></span>www.crestlinesealing.com</div>
  </article>

</main>
</body>
</html>
```